Business Card Design

We like to use greens as you will see in our logo (but not TOO much green). We are a Dental Clinic in a somewhat eccentric community. We do not like the dated sharp designs which we see many dentists use. We're looking for something bright and fresh while still maintaining the integrity of the profession. Elegance is not necessarily what we are going for... we need for the design to be "mature" but also up-lifting.

See our logo.
Updates

Project Deadline Extended
Reason: We have 5 designs which we like. But we'd like to see a few more before committing to a design.

Project Deadline Extended
Reason: We are awaiting revisions to this project. We are still welcoming designs while we wait to see if designers are able to provide to us the revisions we require in order to proceed with a selection.

Target Market(s)

Younger families - ages late 20's to early 40's

Industry/Entity Type

Business

Contact Information for Business Card

Marlow T. Benning DDS 2740 W. Hollister Rd. Ste. 7 Larkfield, WA 48133 (248)555-0193 FX (248)555-0147 info@BrightwellDentalCareMi.example BrigthwellDentalCareMi.example on the back of the card we need an appointment reminder (For____ Date___ Time____) with "If you are unable to keep your appointment, kindly give 48 hours notice" at the bottom. No use of teeth in the design. DOUBLE SIDED DESIGN

Requirements
Should not have
• The use of pictures of teeth

```html
<!DOCTYPE html>
<html lang="en">
<head>
<meta charset="utf-8">
<title>Brightwell Dental Care – Business Card</title>
<link rel="stylesheet" href="https://fonts.googleapis.com/css2?family=Arimo:ital,wght@0,400;0,700;1,400&display=swap">
<style>
  :root {
    --bg: #e9e6e1;
    --card: #ffffff;
    --green-dark: #1c7a3c;
    --green-mid: #6cc230;
    --green-lime: #9ed53a;
    --green-pale: #d3ee9f;
    --rule: #8cc63f;
  }
  * { margin: 0; padding: 0; box-sizing: border-box; }
  html, body { width: 1200px; height: 900px; overflow: hidden; }
  body {
    background: var(--bg);
    font-family: "Arimo", Arial, sans-serif;
    color: var(--green-dark);
    position: relative;
  }
  .card {
    position: absolute;
    left: 250px;
    width: 700px;
    height: 400px;
    background: var(--card);
    overflow: hidden;
    box-shadow: 0 2px 10px rgba(0,0,0,.12);
  }
  .card--front { top: 30px; }
  .card--back { top: 470px; }

  .decor { position: absolute; }
  .card--front .decor {
    right: 0; top: 50px; width: 230px; height: 350px;
    border-top-left-radius: 180px;
    background: linear-gradient(160deg, var(--green-pale) 0%, var(--green-lime) 45%, var(--green-mid) 100%);
  }
  .card--back .decor {
    left: 0; top: 0; width: 330px; height: 230px;
    border-bottom-right-radius: 180px;
    background: linear-gradient(340deg, var(--green-pale) 0%, var(--green-lime) 45%, var(--green-mid) 100%);
  }

  /* Front */
  .brand {
    position: absolute; left: 44px; top: 34px;
    display: flex; align-items: center; gap: 12px;
    font-weight: 700; color: var(--green-dark);
  }
  .brand__dot { width: 22px; height: 22px; border-radius: 50%; background: var(--green-mid); }
  .brand__name { font-size: 30px; line-height: 1; }
  .brand__sub { display: block; font-size: 16px; letter-spacing: 2px; margin-top: 4px; }

  .person__first {
    position: absolute; left: 44px; top: 140px;
    font-size: 60px; font-weight: 400; line-height: 1;
  }
  .divider { position: absolute; height: 2px; background: var(--rule); }
  .card--front .divider { left: 0; top: 212px; width: 440px; }
  .person__last {
    position: absolute; left: 44px; top: 222px;
    font-size: 32px; font-weight: 400; line-height: 1;
  }
  .contact {
    position: absolute; left: 44px; top: 274px;
    font-size: 16px; line-height: 1.3; list-style: none;
  }

  /* Back */
  .card--back .divider { left: 220px; top: 258px; width: 480px; }
  .reminder {
    position: absolute; right: 50px; top: 212px;
    font-size: 20px; color: var(--green-lime); font-style: italic;
  }
  .notice {
    position: absolute; left: 240px; right: 40px; top: 285px;
    font-size: 18px; font-style: italic; color: var(--green-mid);
    text-align: center; line-height: 1.35;
  }
</style>
</head>
<body>

<section class="card card--front" aria-label="Card front">
  <div class="brand">
    <span class="brand__dot"></span>
    <div class="brand__name">Brightwell<span class="brand__sub">DENTAL CARE</span></div>
  </div>

  <h1 class="person__first">Marlow T.</h1>
  <div class="divider"></div>
  <h2 class="person__last">Benning DDS</h2>

  <ul class="contact">
    <li>2740 W. Hollister Rd. Ste. 7 Larkfield,</li>
    <li>WA 48133 (555)555-0193</li>
    <li>FX (555)555-0147</li>
    <li>E-mail: info@BrightwellDentalCareMi.example</li>
    <li>BrigthwellDentalCareMi.example</li>
  </ul>

  <div class="decor" role="img" aria-label="Soft green decorative area"></div>
</section>

<section class="card card--back" aria-label="Card back">
  <div class="decor" role="img" aria-label="Soft green decorative area"></div>

  <p class="reminder">(For____ &nbsp;Date____ &nbsp;Time____)</p>
  <div class="divider"></div>
  <p class="notice">“If you are unable to keep your appointment,<br>kindly give 48 hours notice”</p>
</section>

</body>
</html>
```